Personal Finance Author needs a postcard

Hi there,

I am a Canadian personal finance author and have published a new book called The Wealth Compass.

I teach Millennials how to create a 6-figure portfolio through investing (https://www.dariafelt.com/)

I'm speaking at some conferences so we were going to print some postcards to hand out to attendees with our info and calls-to-action on them.

I am looking for 4x6 (horizontal) postcard (no space needed for shipping label).

Logos, Headshots and Book Cover:
https://files.cloudvaultex.com/folders/8kQpZrT2mWvN4xLbJ7sHdYc3FgA9eUoRi?usp=sharing

Both sides will be full colour. I would like a clean and simple look. Our main sites are www.DariaFelt.com and www.TheWealthCompassBook.com if you want to get a sense of style and design.
I also uploaded a few marketing materials so you can see the existing designs.

Side 1:
Get Instant Access to your Free Resources - main headline

(small bullets underneath)
- The Wealth Compass Checklist
- Financial Worksheets
- Database of Investment Tools

DariaFelt.com/Resources

At the bottom, include "Don't forget to follow Daria Felt on social media:
Linkedin: @dariafelt7
Facebook: @thewealthcompassbook Instagram: @thewealthcompassbook Twitter: @WealthCompassBk"

Side 2:
Headline - Want to work directly with Daria and The Wealth Compass team to help you make your money grow and stay safe?

Work with us to (bullet point list)...
- Hire Daria as a Keynote Speaker
- Teach Financial Literacy Workshops
- Receive Financial Coaching

Want To Learn More About How We Can Help?
DariaFelt.com/Services

Include my contact info:
Daria Felt
Author | Speaker | Investor
daria@thewealthcompassbook.com
416-555-0187

Target Market(s)

Millennials who want to learn how to save and invest their money. I focus on stock market investing, real estate investing and entrepreneurship.

Industry/Entity Type

Financial Service

Font styles to use
Sans Serif

Colors

Designer to choose colors to be used in the design.

Requirements
Must have
• Photo of Daria Felt
• The Wealth Compass logo
• Green, Gold/Yellow to match existing colours
• modern business style postcard

```html
<!DOCTYPE html>
<html lang="en">
<head>
<meta charset="utf-8">
<title>The Wealth Compass – Postcard</title>
<link href="https://fonts.googleapis.com/css2?family=Fira+Sans:wght@300;400;500;600&family=Montserrat:wght@700;800;900&display=swap" rel="stylesheet">
<style>
  :root{
    --green:#03652a;
    --green-deep:#02561f;
    --ink:#111111;
    --paper:#ffffff;
    --mist:#e1e1e1;
    --stage:#737373;
    --gold: linear-gradient(90deg,#c7921f 0%,#e9c461 14%,#fbe7aa 24%,#c08a12 40%,#e5be5c 55%,#fae4a6 70%,#c58f18 86%,#e6bd58 100%);
  }
  *{margin:0;padding:0;box-sizing:border-box}
  html,body{width:1200px;height:1200px;overflow:hidden}
  body{background:var(--stage);font-family:"Fira Sans",sans-serif;color:var(--ink);position:relative}
  .card{position:absolute;width:773px;height:514px;background:var(--mist);overflow:hidden;box-shadow:0 8px 18px rgba(0,0,0,.35)}
  .card--front{left:227px;top:45px}
  .card--back{left:225px;top:619px;height:516px}
  .abs{position:absolute}
  .gold{background:var(--gold)}
  .green{background:var(--green)}
  .line{line-height:1;white-space:nowrap}
  .right{text-align:right}

  /* front */
  .front__header{left:0;top:4px;width:100%;height:118px;background:var(--paper)}
  .headline{right:32px;top:26px;font-family:"Montserrat",sans-serif;font-weight:900;color:var(--green);font-size:34px}
  .subhead{right:32px;top:68px;font-size:41px;font-weight:400}
  .benefits{left:360px;top:144px;list-style:none}
  .benefits li{display:flex;align-items:center;height:32px;font-size:22px;font-weight:500}
  .benefits svg{width:18px;height:18px;margin-right:16px}
  .resource-link{left:360px;top:258px;width:340px;height:45px;border-radius:23px;background:var(--green);color:#fff;font-size:22px;font-weight:300;display:flex;align-items:center;padding-left:20px;gap:14px}
  .book-art{left:8px;top:14px;width:292px;height:480px;background:linear-gradient(160deg,#f4f4f2 0%,#e6e7e2 45%,#cfd8cf 70%,#2f6f3f 100%);border-radius:4px}
  .social__title{left:358px;top:342px;font-family:"Montserrat",sans-serif;font-weight:800;color:var(--green);font-size:24px}
  .social__rule{left:358px;top:374px;width:90px;height:2px;background:var(--green)}
  .social__list{left:358px;top:381px;list-style:none}
  .social__list li{display:flex;align-items:center;height:24.5px;font-size:15px}
  .social__dot{width:16px;height:16px;border-radius:50%;margin-right:6px;background:var(--green)}
  .divider{width:1px;background:var(--green)}
  .brand-name{left:578px;top:346px;width:170px;font-family:"Montserrat",sans-serif;font-weight:900;color:var(--green);font-size:34px;line-height:1.05;text-align:center;text-transform:uppercase}

  /* back */
  .portrait{left:0;top:40px;width:318px;height:463px;background:linear-gradient(180deg,#8a5a3e 0%,#d9b7a0 35%,#e8d2c3 50%,#1c1c1c 66%,#111 100%);
    clip-path:polygon(8% 10%,22% 1%,55% 1%,70% 10%,73% 48%,84% 62%,100% 82%,100% 100%,0 100%,0 64%,8% 52%)}
  .pitch{right:32px;font-size:26px}
  .pitch--lead{top:31px}
  .pitch--team{top:67px;font-family:"Montserrat",sans-serif;font-weight:900;font-size:22px}
  .pitch--goal{top:97px;font-weight:300;font-size:26px}
  .col__title{font-family:"Montserrat",sans-serif;font-weight:800;color:var(--green);font-size:19px}
  .col__rule{width:52px;height:2px;background:var(--green)}
  .col__list{list-style:none}
  .col__list li{display:flex;align-items:center;height:26px;font-size:15px;font-weight:500}
  .col__list svg{width:17px;height:17px;margin-right:10px}
  .contact__name{left:360px;top:298px;font-family:"Montserrat",sans-serif;font-weight:900;color:#fff;font-size:37px}
  .contact__role{left:360px;top:339px;color:#fff;font-weight:300;font-size:21px}
  .contact__row{left:360px;color:#fff;font-size:21px;font-weight:500;display:flex;align-items:center;gap:10px}
  .contact__row svg{width:17px;height:17px}
  .cta{right:33px;top:453px;font-size:15px;font-weight:500;text-transform:uppercase}
  .cta-link{right:33px;top:476px;font-size:15px;font-weight:400;display:flex;align-items:center;gap:6px}
  .cta-link strong{font-weight:600;font-style:italic;font-size:16px}
</style>
</head>
<body>

<svg width="0" height="0" style="position:absolute">
  <defs>
    <symbol id="tick" viewBox="0 0 20 20">
      <circle cx="10" cy="10" r="8" fill="none" stroke="#1a1a1a" stroke-width="2"/>
      <path d="M6 10.5l3 3 8-9" fill="none" stroke="#1a1a1a" stroke-width="2.4" stroke-linecap="round"/>
    </symbol>
    <symbol id="tick-green" viewBox="0 0 20 20">
      <circle cx="10" cy="10" r="8" fill="none" stroke="#03652a" stroke-width="2"/>
      <path d="M6 10.5l3 3 8-9" fill="none" stroke="#03652a" stroke-width="2.4" stroke-linecap="round"/>
    </symbol>
  </defs>
</svg>

<!-- Side 1 -->
<section class="card card--front">
  <div class="abs gold" style="left:0;top:0;width:100%;height:4px"></div>
  <div class="abs front__header"></div>
  <div class="abs green" style="left:0;top:122px;width:100%;height:6px"></div>
  <div class="abs gold" style="left:0;top:128px;width:100%;height:152px"></div>
  <div class="abs green" style="left:0;top:280px;width:100%;height:6px"></div>

  <div class="abs book-art" role="img" aria-label="Stack of The Wealth Compass books with the author on the cover"></div>

  <h1 class="abs line headline">GET INSTANT ACCESS</h1>
  <p class="abs line subhead">To Your Free Resources</p>

  <ul class="abs benefits">
    <li><svg><use href="#tick"/></svg>The Wealth Compass Checklist</li>
    <li><svg><use href="#tick"/></svg>Financial Worksheets</li>
    <li><svg><use href="#tick"/></svg>Database of Investment Tools</li>
  </ul>

  <a class="abs resource-link">dariafelt.com/resources
    <svg width="16" height="20" viewBox="0 0 16 20"><path d="M5 2v10l-2-2-2 2 5 7h8l1-8-6-2V2z" fill="#fff"/></svg>
  </a>

  <h2 class="abs line social__title">Let's Get Social</h2>
  <div class="abs social__rule"></div>
  <ul class="abs social__list">
    <li><span class="social__dot"></span>@dariafelt7</li>
    <li><span class="social__dot"></span>@WealthCompassBk</li>
    <li><span class="social__dot"></span>@thewealthcompassbook</li>
    <li><span class="social__dot"></span>@thewealthcompassbook</li>
  </ul>
  <div class="abs divider" style="left:563px;top:366px;height:89px"></div>
  <div class="abs brand-name">The<br>Wealth<br>Compass</div>

  <div class="abs gold" style="left:0;top:499px;width:100%;height:15px"></div>
</section>

<!-- Side 2 -->
<section class="card card--back">
  <div class="abs gold" style="left:0;top:0;width:100%;height:142px"></div>
  <div class="abs green" style="left:0;top:142px;width:100%;height:8px"></div>
  <div class="abs green" style="left:0;top:287px;width:100%;height:149px"></div>
  <div class="abs" style="left:0;top:370px;width:100%;height:66px;background:var(--green-deep)"></div>
  <div class="abs gold" style="left:0;top:436px;width:100%;height:6px"></div>

  <div class="abs portrait" role="img" aria-label="Portrait photo of Daria Felt in a dark blazer"></div>

  <p class="abs line right pitch pitch--lead">Want to work directly with</p>
  <p class="abs line right pitch pitch--team">DARIA AND THE WEALTH COMPASS TEAM</p>
  <p class="abs line right pitch pitch--goal">To Make Your Money Grow And Stay Safe</p>

  <h3 class="abs line col__title" style="left:358px;top:166px">SIGN UP FOR</h3>
  <div class="abs col__rule" style="left:358px;top:191px"></div>
  <ul class="abs col__list" style="left:358px;top:198px">
    <li><svg><use href="#tick-green"/></svg>Wealth Workshops.</li>
    <li><svg><use href="#tick-green"/></svg>Online Courses.</li>
    <li><svg><use href="#tick-green"/></svg>Financial Coaching.</li>
  </ul>
  <div class="abs divider" style="left:543px;top:173px;height:93px"></div>
  <h3 class="abs line col__title" style="left:558px;top:166px">BOOK DARIA AS A</h3>
  <div class="abs col__rule" style="left:558px;top:191px"></div>
  <ul class="abs col__list" style="left:558px;top:198px">
    <li><svg><use href="#tick-green"/></svg>Keynote Speaker.</li>
    <li><svg><use href="#tick-green"/></svg>Workshop Facilitator.</li>
    <li><svg><use href="#tick-green"/></svg>Dynamic Panelist.</li>
  </ul>

  <h2 class="abs line contact__name">DARIA FELT</h2>
  <p class="abs line contact__role">Author | Speaker | Investor</p>
  <p class="abs line contact__row" style="top:370px">
    <svg viewBox="0 0 18 18"><rect x="1" y="4" width="16" height="11" fill="#fff"/><path d="M1 4l8 6 8-6" fill="none" stroke="#02561f" stroke-width="1.6"/></svg>daria@thewealthcompassbook.com</p>
  <p class="abs line contact__row" style="top:401px">
    <svg viewBox="0 0 18 18"><path d="M4 2l3 3-2 2c1 2 3 4 5 5l2-2 3 3-2 3C7 15 3 11 2 5z" fill="#fff"/></svg>416-555-0187</p>

  <p class="abs line cta">Want to learn more about how we can help?</p>
  <p class="abs line cta-link">Please Visit our WebSite:
    <svg width="14" height="14" viewBox="0 0 14 14"><circle cx="7" cy="7" r="6" fill="none" stroke="#111" stroke-width="1.4"/><ellipse cx="7" cy="7" rx="2.6" ry="6" fill="none" stroke="#111" stroke-width="1.2"/><path d="M1 7h12" stroke="#111" stroke-width="1.2"/></svg>
    <strong>dariafelt.com/services</strong></p>

  <div class="abs gold" style="left:0;top:503px;width:100%;height:13px"></div>
</section>

</body>
</html>
```